Business Card for By Karel Voss

Looking to have a business card designed for my lifestyle and fitness company. My company offers personal training, online programming and nutrition advice based out of London, United Kingdom.

I'd like to see modern, sleek designs, focusing on black, matte black or matte grey. Design doesn't need to be overly descriptive as this will also be used as a personal business card. I've included my logo.

Please note that my company is no longer called "Fitness by Karel Voss" but instead "By Karel Voss", this is because of my other ventures. Therefore please don't use the "fitness by karel voss" text.

information about my company can be found at www.bykarelvoss.com

Company is also based out of London (United Kingdom) & Sydney (Australia) this could be reflected on the card.

Industry/Entity Type

Business

Contact Information for Business Card

Karel Voss
+44 7382 615027
karel@bykarelvoss.com
www.bykarelvoss.com

Font styles to use
Sans Serif

Requirements
Must have
• All contact details and inclusion of my logo.

```html
<!DOCTYPE html>
<html lang="en">
<head>
<meta charset="utf-8">
<title>By Karel Voss — Business Card</title>
<link rel="stylesheet" href="https://fonts.googleapis.com/css2?family=Montserrat:wght@300;400;600;800&display=swap">
<style>
  :root {
    --stage: #3a3a3a;
    --card-black: #1b1b1b;
    --card-white: #ffffff;
    --ink-light: #f2f2f2;
    --ink-muted: #cfcfcf;
    --ink-dark: #151515;
  }
  * { margin: 0; padding: 0; box-sizing: border-box; }
  html, body { width: 1200px; height: 1028px; overflow: hidden; }
  body {
    background: var(--stage);
    font-family: "Montserrat", sans-serif;
    position: relative;
  }
  .card {
    position: absolute;
    width: 540px;
    height: 308px;
    border-radius: 4px;
    overflow: hidden;
    box-shadow: 0 12px 30px rgba(0,0,0,0.45);
  }
  .card--front { left: 40px; top: 560px; display: flex; background: var(--card-black); }
  .card--back { left: 620px; top: 160px; background: var(--card-black); display: flex; align-items: center; justify-content: center; }

  .brand {
    display: flex;
    align-items: center;
    gap: 10px;
    font-weight: 800;
    text-transform: uppercase;
    letter-spacing: 1px;
    white-space: nowrap;
  }
  .brand__dot { width: 12px; height: 12px; border-radius: 50%; background: currentColor; flex: none; }
  .brand--light { color: var(--ink-light); font-size: 34px; }
  .brand--light .brand__dot { width: 14px; height: 14px; }
  .brand--dark { color: var(--ink-dark); font-size: 17px; }
  .brand--dark .brand__dot { width: 10px; height: 10px; }

  .front__logo-panel {
    width: 44%;
    padding: 0 24px;
    background: var(--card-white);
    display: flex;
    align-items: center;
    justify-content: center;
  }
  .front__details {
    flex: 1;
    padding: 44px 0 0 36px;
    color: var(--ink-light);
  }
  .person__name { font-size: 22px; font-weight: 300; }
  .person__name strong { font-weight: 600; }
  .person__title { font-size: 13px; font-weight: 300; color: var(--ink-muted); margin-top: 2px; letter-spacing: 0.5px; }
  .person__rule { width: 40px; height: 3px; background: var(--ink-light); margin: 12px 0 22px; }
  .contact { list-style: none; }
  .contact__item { display: flex; align-items: center; gap: 12px; font-size: 14px; font-weight: 400; margin-bottom: 13px; white-space: nowrap; }
  .contact__icon { width: 15px; height: 15px; flex: none; }
</style>
</head>
<body>

  <section class="card card--front" aria-label="Business card front">
    <div class="front__logo-panel">
      <div class="brand brand--dark"><span class="brand__dot"></span>By Karel Voss</div>
    </div>
    <div class="front__details">
      <p class="person__name"><strong>Karel</strong> Voss</p>
      <p class="person__title">Managing Director</p>
      <div class="person__rule"></div>
      <ul class="contact">
        <li class="contact__item">
          <svg class="contact__icon" viewBox="0 0 16 16" fill="none" stroke="currentColor" stroke-width="1.6"><path d="M3 2h3l1 3-2 1a9 9 0 0 0 5 5l1-2 3 1v3a1 1 0 0 1-1 1A12 12 0 0 1 2 3a1 1 0 0 1 1-1z"/></svg>
          +44 7382 615027
        </li>
        <li class="contact__item">
          <svg class="contact__icon" viewBox="0 0 16 16" fill="none" stroke="currentColor" stroke-width="1.6"><rect x="1.5" y="3.5" width="13" height="9"/><path d="M1.5 3.5 8 9l6.5-5.5"/></svg>
          karel@bykarelvoss.com
        </li>
        <li class="contact__item">
          <svg class="contact__icon" viewBox="0 0 16 16" fill="none" stroke="currentColor" stroke-width="1.4"><circle cx="8" cy="8" r="6.5"/><ellipse cx="8" cy="8" rx="2.8" ry="6.5"/><path d="M1.5 8h13"/></svg>
          www.bykarelvoss.com
        </li>
      </ul>
    </div>
  </section>

  <section class="card card--back" aria-label="Business card back">
    <div class="brand brand--light"><span class="brand__dot"></span>By Karel Voss</div>
  </section>

</body>
</html>
```